Business card for event manager / organizer "waiter service"

Draft of a new valuable business card for my company.
Events, personnel service providers, festivals

```html
<!DOCTYPE html>
<html lang="de">
<head>
<meta charset="utf-8">
<title>Nico´s Kellnerservice – Visitenkarte</title>
<link rel="stylesheet" href="https://fonts.googleapis.com/css2?family=Arimo:wght@400;700&display=swap">
<style>
  :root {
    --page: #e8e8e8;
    --card-dark: #2f2f2f;
    --card-darker: #242424;
    --orange: #e8731c;
    --orange-deep: #b5470f;
    --white: #f4f4f4;
    --muted: #cfcfcf;
    --photo-shirt: #1b2430;
  }
  * { box-sizing: border-box; margin: 0; padding: 0; }
  html, body { width: 1200px; height: 802px; overflow: hidden; }
  body {
    background: var(--page);
    font-family: "Arimo", Arial, sans-serif;
    display: flex;
    align-items: center;
    justify-content: center;
    gap: 48px;
  }
  .card {
    width: 540px;
    height: 348px;
    position: relative;
    overflow: hidden;
    box-shadow: 0 6px 18px rgba(0,0,0,.25);
  }

  /* Contact side */
  .card--contact { background: var(--card-dark); }
  .portrait {
    position: absolute;
    left: 0; bottom: 0;
    width: 250px; height: 230px;
    background: linear-gradient(180deg, #3a3a3a 0%, var(--photo-shirt) 55%, #141a22 100%);
    border-top-right-radius: 120px 100px;
  }
  .brand {
    position: absolute;
    right: 28px; top: 26px;
    display: flex; align-items: center; gap: 10px;
  }
  .brand__mark { width: 22px; height: 22px; background: var(--orange); }
  .brand__name {
    color: var(--white); font-weight: 700; font-size: 22px;
    letter-spacing: .5px; line-height: 1;
  }
  .brand__tagline {
    position: absolute; right: 28px; top: 56px;
    color: var(--muted); font-size: 9px;
  }
  .contact {
    position: absolute; right: 28px; top: 92px;
    text-align: right;
  }
  .contact__name { color: var(--orange); font-weight: 700; font-size: 23px; }
  .contact__role { color: var(--white); font-size: 13px; margin: 2px 0 10px; }
  .contact__list { list-style: none; }
  .contact__item {
    color: var(--white); font-size: 13px; line-height: 19px;
    display: flex; justify-content: flex-end; align-items: center; gap: 8px;
  }
  .contact__icon { width: 12px; height: 12px; flex: none; }
  .address-band {
    position: absolute; right: 0; bottom: 0;
    width: 300px; height: 40px;
    background: linear-gradient(90deg, var(--orange) 0%, var(--orange-deep) 100%);
    clip-path: polygon(24px 0, 100% 0, 100% 100%, 0 100%);
    color: var(--white); font-size: 13px;
    display: flex; align-items: center; justify-content: flex-end;
    padding-right: 28px;
  }

  /* Front side */
  .card--front { background: var(--card-darker); }
  .crowd {
    position: absolute; inset: 0;
    background: linear-gradient(180deg, var(--card-darker) 0%, #4a3a30 35%, #c26a2c 60%, #7a2a10 85%, #3a150a 100%);
    z-index: 0;
  }
  .front-brand {
    position: absolute; left: 56px; top: 92px;
    z-index: 1;
  }
  .front-brand__row { display: flex; align-items: center; gap: 14px; }
  .front-brand__mark { width: 40px; height: 40px; background: var(--orange); flex: none; }
  .front-brand__name {
    color: var(--white); font-weight: 700; font-size: 38px;
    line-height: 1; letter-spacing: .5px;
  }
  .front-brand__tagline {
    color: var(--muted); font-size: 12px; margin: 8px 0 0 54px;
  }
</style>
</head>
<body>

  <section class="card card--contact">
    <div class="portrait" role="img" aria-label="Porträtfoto des Inhabers im dunklen Hemd"></div>

    <div class="brand">
      <span class="brand__mark"></span>
      <span class="brand__name">NICO´S KELLNERSERVICE</span>
    </div>
    <p class="brand__tagline">…denn die nächste Party wartet schon!</p>

    <div class="contact">
      <p class="contact__name">Nico Bergmann</p>
      <p class="contact__role">Inhaber</p>
      <ul class="contact__list">
        <li class="contact__item">02361 555 20 40
          <svg class="contact__icon" viewBox="0 0 12 12"><circle cx="6" cy="6" r="6" fill="var(--orange)"/><path d="M3.5 3.2c.4-.4.9-.4 1.1 0l.6 1c.2.3 0 .6-.2.8l-.3.3c.4.8 1 1.4 1.8 1.8l.3-.3c.2-.2.5-.4.8-.2l1 .6c.4.2.4.7 0 1.1-.6.6-1.5.7-2.4.1-1.1-.7-2.2-1.8-2.9-2.9-.5-.9-.4-1.8.2-2.3z" fill="var(--card-dark)"/></svg>
        </li>
        <li class="contact__item">0171 555 83 12
          <svg class="contact__icon" viewBox="0 0 12 12"><circle cx="6" cy="6" r="6" fill="var(--orange)"/><rect x="4" y="2.5" width="4" height="7" rx="0.8" fill="var(--card-dark)"/></svg>
        </li>
        <li class="contact__item">info@nicos-kellnerservice.de
          <svg class="contact__icon" viewBox="0 0 12 12"><rect x="0.5" y="2" width="11" height="8" fill="var(--orange)"/><path d="M0.5 2l5.5 4.5L11.5 2" fill="none" stroke="var(--card-dark)" stroke-width="1"/></svg>
        </li>
        <li class="contact__item">www.nicos-kellnerservice.de
          <svg class="contact__icon" viewBox="0 0 12 12"><circle cx="6" cy="6" r="5.5" fill="var(--orange)"/><path d="M0.5 6h11M6 .5c-2.5 3-2.5 8 0 11M6 .5c2.5 3 2.5 8 0 11" fill="none" stroke="var(--card-dark)" stroke-width=".8"/></svg>
        </li>
        <li class="contact__item">nicoskellnerservice
          <svg class="contact__icon" viewBox="0 0 12 12"><circle cx="6" cy="6" r="6" fill="var(--orange)"/></svg>
        </li>
      </ul>
    </div>

    <div class="address-band">Lindenweg 12, 45701 Musterstadt</div>
  </section>

  <section class="card card--front">
    <div class="crowd" role="img" aria-label="Foto einer feiernden Menge mit erhobenen Händen vor orangefarbener Bühnenbeleuchtung"></div>
    <div class="front-brand">
      <div class="front-brand__row">
        <span class="front-brand__mark"></span>
        <span class="front-brand__name">NICO´S<br>KELLNERSERVICE</span>
      </div>
      <p class="front-brand__tagline">…denn die nächste Party wartet schon!</p>
    </div>
  </section>

</body>
</html>
```